QM Candle Tube Packaging Design

Website: www.quorelmaren.com
IG: @quorel.maren
Tagline: Elevate Your Ambiance
My brand is a sophisticated brand with luxury candles made of coconut wax. Im looking for an upscale minimalist chic design.
Discover the transformative power of positive energy with Quorel Maren candles. Indulge in true luxury with our specially crafted coconut wax blend that not only ignites captivating scents but also embodies modern elegance and empowering elements.
At Quorel Maren we're committed to delivering a unique and exhilarating aromatic experience to all candle lovers. Each candle is meticulously handcrafted in small batches using luxury fragrance oils exclusively formulated for coconut wax.
Our candles are:
Clean-burning
Paraben-Free
Phthalate-Free
Skin-Safe
Pet-Friendly

```html
<!DOCTYPE html>
<html lang="en">
<head>
<meta charset="utf-8">
<title>Quorel Maren – Candle Label</title>
<link rel="stylesheet" href="https://fonts.googleapis.com/css2?family=Allura&family=Mrs+Saint+Delafield&family=Poppins:wght@300;400&display=swap">
<style>
  :root {
    --backdrop: #f2f1ef;
    --label-top: #fefcf3;
    --label-bottom: #f7f0de;
    --ink: #2b2a28;
    --terracotta: #c98a66;
    --sage: #8fa173;
    --frame: #3a3936;
  }
  * { margin: 0; padding: 0; box-sizing: border-box; }
  html, body { width: 1200px; height: 2400px; overflow: hidden; background: var(--backdrop); }
  .canvas { position: relative; width: 1200px; height: 2400px; }
  .label {
    position: absolute; left: 120px; top: 420px; width: 960px; height: 1560px;
    background: linear-gradient(to bottom, var(--label-top) 0 907px, var(--label-bottom) 907px 100%);
    box-shadow: 0 14px 30px rgba(0,0,0,0.18);
    font-family: "Poppins", sans-serif; color: var(--ink);
  }
  .label > * { position: absolute; left: 0; width: 100%; text-align: center; }
  .brand-name { top: 318px; font-weight: 300; font-size: 66px; letter-spacing: 2px; line-height: 1; text-transform: uppercase; }
  .brand-line { top: 420px; font-size: 21px; letter-spacing: 8px; font-weight: 400; }
  .brand-line::before, .brand-line::after { content: ""; display: inline-block; width: 32px; height: 2px; background: var(--ink); vertical-align: middle; margin: 0 16px; }
  .brand-whisper { top: 452px; font-family: "Mrs Saint Delafield", cursive; font-size: 30px; }
  .frame { top: 0; height: 100%; pointer-events: none; }
  .tag-script { top: 540px; font-family: "Allura", cursive; font-size: 170px; color: var(--terracotta); line-height: 1; }
  .tag-your { top: 700px; font-weight: 300; font-size: 84px; color: var(--terracotta); line-height: 1; letter-spacing: 2px; }
  .tag-ambiance { top: 780px; font-weight: 300; font-size: 106px; color: var(--sage); line-height: 1; letter-spacing: 3px; }
  .benefit { width: 180px; text-align: center; font-size: 27px; line-height: 1.2; }
  .benefit svg { display: block; margin: 0 auto 8px; }
  .product-type { top: 1344px; font-size: 27px; letter-spacing: 7px; font-weight: 400; }
  .product-weight { top: 1392px; font-size: 29px; font-weight: 400; }
</style>
</head>
<body>
<main class="canvas">
  <section class="label">
    <svg class="frame" width="960" height="1560" viewBox="0 0 960 1560">
      <g stroke="var(--frame)" stroke-width="2" fill="none">
        <polyline points="284,567 105,567 105,1365 239,1365"/>
        <polyline points="689,567 859,567 859,1365 717,1365"/>
      </g>
    </svg>

    <h1 class="brand-name">Quorel Maren</h1>
    <p class="brand-line">HANDMADE CANDLES</p>
    <p class="brand-whisper">with purpose and love</p>

    <p class="tag-script">Elevate</p>
    <p class="tag-your">YOUR</p>
    <p class="tag-ambiance">AMBIANCE</p>

    <div class="benefit" style="left:203px; top:935px;">
      <svg width="92" height="92" viewBox="0 0 92 92"><circle cx="46" cy="46" r="44" fill="none" stroke="var(--terracotta)" stroke-width="3"/><path d="M46 22c8 12 16 18 16 30a16 16 0 0 1-32 0c0-8 6-12 8-18 3 6 4 8 6 10 2-8 2-14 2-22z" fill="none" stroke="var(--sage)" stroke-width="2"/></svg>
      Clean<br>burning
    </div>
    <div class="benefit" style="left:394px; top:935px;">
      <svg width="92" height="92" viewBox="0 0 92 92"><circle cx="46" cy="46" r="44" fill="none" stroke="var(--terracotta)" stroke-width="3"/><circle cx="46" cy="46" r="24" fill="none" stroke="var(--terracotta)" stroke-width="2"/><path d="M41 32h10M43 32v10l-7 14h20l-7-14V32" fill="none" stroke="var(--sage)" stroke-width="2"/><line x1="29" y1="29" x2="63" y2="63" stroke="var(--terracotta)" stroke-width="2"/></svg>
      Paraben<br>Free
    </div>
    <div class="benefit" style="left:594px; top:935px;">
      <svg width="92" height="92" viewBox="0 0 92 92"><circle cx="46" cy="46" r="44" fill="none" stroke="var(--terracotta)" stroke-width="3"/><circle cx="46" cy="46" r="28" fill="none" stroke="var(--sage)" stroke-width="1.5"/><path d="M46 30c6 9 10 13 10 19a10 10 0 0 1-20 0c0-6 4-10 10-19z" fill="none" stroke="var(--sage)" stroke-width="2"/></svg>
      Phthalate<br>Free
    </div>
    <div class="benefit" style="left:294px; top:1125px;">
      <svg width="92" height="92" viewBox="0 0 92 92"><circle cx="46" cy="46" r="44" fill="none" stroke="var(--terracotta)" stroke-width="3"/><path d="M46 26l18 6v12c0 12-8 20-18 24-10-4-18-12-18-24V32z" fill="none" stroke="var(--sage)" stroke-width="2"/><path d="M46 40v14M39 47h14" stroke="var(--sage)" stroke-width="2"/></svg>
      Skin-Safe
    </div>
    <div class="benefit" style="left:477px; top:1125px;">
      <svg width="92" height="92" viewBox="0 0 92 92"><circle cx="46" cy="46" r="44" fill="none" stroke="var(--terracotta)" stroke-width="3"/><path d="M46 64L28 46a10 10 0 0 1 18-12 10 10 0 0 1 18 12z" fill="none" stroke="var(--sage)" stroke-width="2"/></svg>
      Pet<br>Friendly
    </div>

    <p class="product-type">COCONUT WAX CANDLE</p>
    <p class="product-weight">14OZ. (396G)</p>
  </section>
</main>
</body>
</html>
```